Records Management Company Revamp

We are looking to revamp our web presence, and need a catchy design that helps us to get noticed! We would like the website to be in wordpress. the main requirements are a home page, a landing page template for SEO / PPC, and then a few other pages that can be reused throughout the website.

We are happy to supply content / video etc.

Number of Pages Required

3 page

Font styles to use
Other font styles liked:
• Find fonts listed in attached branding document

Requirements
Must have
• Home page as well as sub pages according to their colours. Need to use colours and fonts set out in branding guide. Attached are examples of home page and sub pages.
Nice to have
• We have uploaded some very basic ideas we have of how we wish the website to look, but looking to have it more professional and fit together. Please see uploaded items.

```html
<!DOCTYPE html>
<html lang="en">
<head>
<meta charset="utf-8">
<title>Keepwell Storage – Archive Document Storage &amp; Records Management</title>
<link href="https://fonts.googleapis.com/css2?family=Oswald:wght@400;500;600&family=Open+Sans:wght@400;600;700&display=swap" rel="stylesheet">
<style>
:root{
  --blue:#2a8fd6;
  --blue-dark:#1f74b4;
  --red:#e0312f;
  --green:#78b52d;
  --orange:#f39a1e;
  --sky:#6fb3dc;
  --ink:#2d2d2d;
  --muted:#7a7a7a;
  --grey:#eeeeee;
  --line:#d9d9d9;
  --footer:#1e1e1e;
  --footer-deep:#141414;
  --white:#ffffff;
}
*{box-sizing:border-box;margin:0;padding:0}
html,body{width:1200px;height:3584px;overflow:hidden}
body{position:relative;background:var(--white);font-family:"Open Sans",Arial,sans-serif;color:var(--ink)}
.abs{position:absolute}
.heading{font-family:"Oswald","Arial Narrow",sans-serif;font-weight:500;letter-spacing:1px}

/* top bar */
.topbar{left:0;top:0;width:1200px;height:32px;background:var(--white);border-bottom:1px solid var(--line)}
.topbar .contact{position:absolute;top:8px;font-size:12px;color:var(--ink);display:flex;align-items:center;gap:8px}
/* header */
.header{left:0;top:32px;width:1200px;height:80px;background:var(--white)}
.brand{position:absolute;left:80px;top:20px;display:flex;align-items:center;gap:10px}
.brand .mark{width:30px;height:30px;background:var(--blue)}
.brand .name{font-family:"Oswald",sans-serif;font-size:22px;font-weight:500;color:var(--ink);line-height:1}
.nav{position:absolute;right:80px;top:32px;display:flex;gap:26px;font-size:12px;font-weight:600;text-transform:uppercase}
.nav a{color:var(--ink);text-decoration:none}
.nav a.active{color:var(--blue);border-bottom:2px solid var(--blue);padding-bottom:4px}

/* hero */
.hero{left:0;top:112px;width:1200px;height:576px;background:linear-gradient(100deg,#3b3a37 0%,#6b6358 45%,#a39786 100%)}
.hero-title{left:80px;top:230px;width:560px;color:var(--white);font-size:40px;line-height:50px;font-weight:500}
.hero-lead{left:80px;top:350px;width:460px;color:var(--white);font-size:20px;line-height:28px;font-weight:700}
.calc{left:752px;top:208px;width:360px;height:396px;background:var(--white);box-shadow:0 4px 14px rgba(0,0,0,.25)}
.calc-head{height:64px;background:var(--blue);color:var(--white);font-size:22px;text-align:center;line-height:64px}
.calc p{font-size:12px;color:var(--muted);text-align:center;padding:16px 30px 8px}
.field{position:absolute;height:38px;border:1px solid var(--line);font-size:11px;color:#9a9a9a;padding:11px 10px}
.calc-btn{position:absolute;right:16px;top:290px;width:44px;height:92px;background:var(--blue)}

/* services */
.service{top:688px;width:240px;height:292px;background:var(--white);box-shadow:0 2px 8px rgba(0,0,0,.15)}
.service .label{height:52px;line-height:52px;text-align:center;color:var(--white);font-size:20px;font-family:"Oswald",sans-serif;text-transform:uppercase}
.service .photo{height:240px}

/* how it works */
.how{left:0;top:1060px;width:1200px;height:710px;background:var(--grey)}
.section-title{font-family:"Oswald",sans-serif;font-size:42px;font-weight:500;color:var(--blue);text-transform:uppercase}
.step{left:80px;width:520px;display:flex;gap:16px}
.step .ico{flex:none;width:42px;height:42px;border-radius:50%;border:2px solid var(--blue);display:flex;align-items:center;justify-content:center}
.step h3{font-size:17px;font-weight:700;color:var(--ink);margin-bottom:4px}
.step p{font-size:11px;line-height:16px;color:var(--muted)}
.how-photo{left:640px;top:1120px;width:480px;height:620px;background:linear-gradient(160deg,#8e6f4d 0%,#c7a679 50%,#6f5a45 100%)}

/* team */
.member{top:1932px;width:240px;height:308px;background:var(--white);border:1px solid var(--line);text-align:center}
.member.featured{border:2px solid var(--sky)}
.member .portrait{margin:16px auto 0;width:206px;height:200px;background:linear-gradient(180deg,#c9ced4,#5e6670)}
.member h4{font-size:16px;font-weight:700;margin-top:16px}
.member p{font-size:12px;color:var(--blue);margin-top:4px}
.team-cta{left:688px;top:1896px;width:412px;height:368px;background:var(--blue);color:var(--white);padding:56px 40px;box-shadow:8px 8px 0 rgba(0,0,0,.08)}
.team-cta h3{font-family:"Oswald",sans-serif;font-weight:500;font-size:28px;line-height:36px;text-align:center;text-transform:uppercase}
.team-cta p{font-size:17px;line-height:24px;font-weight:700;text-align:center;margin-top:16px}
.btn-line{display:inline-flex;align-items:center;gap:16px;border:1px solid var(--white);padding:8px 18px;font-size:13px;font-weight:600;text-transform:uppercase;margin-top:24px;margin-left:72px}

/* why */
.why-item{top:2460px;width:160px;height:164px;border:1px solid var(--line);background:var(--white);text-align:center;padding-top:30px}
.why-item span{display:block;font-size:12px;color:var(--ink);margin-top:14px;line-height:16px}

/* area / testimonials */
.area{left:0;top:2704px;width:600px;height:524px;background:linear-gradient(160deg,#4a4a4a 0%,#2b2b2b 100%)}
.area-text{left:100px;top:2880px;width:420px;color:var(--white);text-align:center}
.area-text h3{font-family:"Oswald",sans-serif;font-weight:500;font-size:38px;letter-spacing:2px;text-transform:uppercase}
.area-text p{font-size:26px;line-height:32px;font-weight:700;margin-top:8px}
.testimonials{left:600px;top:2704px;width:600px;height:524px;background:linear-gradient(135deg,var(--blue-dark),var(--blue))}
.testimonials h3{position:absolute;left:24px;top:80px;font-family:"Oswald",sans-serif;font-weight:500;font-size:38px;color:var(--white);text-transform:uppercase}
.testimonials .who{position:absolute;left:24px;top:220px;font-size:14px;font-weight:700;color:var(--white);text-transform:uppercase}
.testimonials .quote-text{position:absolute;left:24px;top:248px;width:470px;font-size:13px;line-height:19px;color:var(--white)}
.dots{position:absolute;left:24px;top:400px;display:flex;gap:8px}
.dots i{width:8px;height:8px;border-radius:50%;background:rgba(255,255,255,.5)}
.dots i:first-child{background:var(--white)}

/* footer */
.footer{left:0;top:3228px;width:1200px;height:292px;background:var(--footer);color:var(--white)}
.footer h5{font-family:"Oswald",sans-serif;font-weight:500;font-size:22px;text-transform:uppercase}
.footer .links{font-size:12px;line-height:28px;color:#d8d8d8}
.footer .small{font-size:12px;line-height:18px;color:#cfcfcf}
.copyright{left:0;top:3520px;width:1200px;height:64px;background:var(--footer-deep);color:#bdbdbd;font-size:12px;text-align:center;line-height:64px}
</style>
</head>
<body>

<!-- top bar -->
<div class="abs topbar">
  <div class="contact" style="left:770px">
    <svg width="18" height="18" viewBox="0 0 18 18"><circle cx="9" cy="9" r="9" fill="var(--blue)"/><path d="M6 5l2 0 1 3-1.3 1a6 6 0 0 0 2.3 2.3L11 10l3 1v2c-4 .5-8.5-4-8-8z" fill="#fff"/></svg>
    123 456 7890
  </div>
  <div class="contact" style="left:900px">
    <svg width="18" height="18" viewBox="0 0 18 18"><circle cx="9" cy="9" r="9" fill="var(--blue)"/><rect x="4.5" y="6" width="9" height="6.5" fill="#fff"/><path d="M4.5 6l4.5 3.5L13.5 6" stroke="var(--blue)" stroke-width="1" fill="none"/></svg>
    info@keepwell_storage.com
  </div>
</div>

<!-- header -->
<header class="abs header">
  <div class="brand"><div class="mark"></div><div class="name">KEEPWELL STORAGE</div></div>
  <nav class="nav">
    <a class="active" href="#">Home</a>
    <a href="#">Offsite Storage</a>
    <a href="#">Document Shredding</a>
    <a href="#">Digitisation</a>
    <a href="#">Archive Supplies</a>
    <a href="#">Contact</a>
  </nav>
</header>

<!-- hero -->
<section class="abs hero" role="img" aria-label="Warehouse aisles stacked with archive boxes"></section>
<h1 class="abs hero-title heading">ARCHIVE DOCUMENT STORAGE &amp; RECORDS MANAGEMENT</h1>
<p class="abs hero-lead">Professional, secure and reliable. Keepwell Storage is your new home for all your archiving needs.</p>

<form class="abs calc">
  <div class="calc-head heading">PRICE CALCULATOR</div>
  <p>Find out how cost effective we are in storing your archive boxes</p>
  <div class="field" style="left:16px;top:146px;width:160px">Name</div>
  <div class="field" style="left:184px;top:146px;width:160px">Phone</div>
  <div class="field" style="left:16px;top:196px;width:328px">Email</div>
  <div class="field" style="left:16px;top:246px;width:328px">Postcode</div>
  <div class="field" style="left:16px;top:296px;width:264px;height:86px">Approx. Number of Boxes</div>
  <div class="calc-btn">
    <svg width="44" height="92" viewBox="0 0 44 92"><path d="M13 46l18-8-6 18-3-7z" fill="#fff"/></svg>
  </div>
</form>

<!-- services -->
<a class="abs service" style="left:80px"><div class="label" style="background:var(--red)">Offsite Storage</div><div class="photo" role="img" aria-label="Staff member checking archive shelving" style="background:linear-gradient(160deg,#3d6a95,#9bb4c8)"></div></a>
<a class="abs service" style="left:344px"><div class="label" style="background:var(--green)">Document Shredding</div><div class="photo" role="img" aria-label="Shredded paper strips" style="background:linear-gradient(160deg,#e9e9e4,#b9b8b0)"></div></a>
<a class="abs service" style="left:608px"><div class="label" style="background:var(--orange)">Digitisation</div><div class="photo" role="img" aria-label="Archive room with stacked records" style="background:linear-gradient(160deg,#8b7355,#d0b78f)"></div></a>
<a class="abs service" style="left:872px"><div class="label" style="background:var(--sky)">Archive Supplies</div><div class="photo" role="img" aria-label="Flat-packed cardboard archive boxes" style="background:linear-gradient(160deg,#f1ece4,#c9a57a)"></div></a>

<!-- how it works -->
<section class="abs how"></section>
<h2 class="abs section-title" style="left:80px;top:1100px">How it works</h2>
<div class="abs" style="left:80px;top:1160px;width:60px;height:3px;background:var(--blue)"></div>

<div class="abs step" style="top:1190px"><div class="ico"><svg width="22" height="22" viewBox="0 0 22 22"><rect x="3" y="7" width="16" height="11" fill="none" stroke="var(--blue)" stroke-width="2"/><path d="M3 7l3-4h10l3 4" fill="none" stroke="var(--blue)" stroke-width="2"/></svg></div><div><h3>We deliver boxes and Barcodes</h3><p>If you need them, we get you started with all the essentials to prepare your archives.</p></div></div>
<div class="abs step" style="top:1296px"><div class="ico"><svg width="22" height="22" viewBox="0 0 22 22"><rect x="2" y="7" width="12" height="9" fill="none" stroke="var(--blue)" stroke-width="2"/><path d="M14 10h4l2 3v3h-6" fill="none" stroke="var(--blue)" stroke-width="2"/></svg></div><div><h3>We pick up your documents</h3><p>When your boxes are ready, let us know and we'll come by and collect your documents.</p></div></div>
<div class="abs step" style="top:1402px"><div class="ico"><svg width="22" height="22" viewBox="0 0 22 22"><rect x="4" y="3" width="14" height="16" fill="none" stroke="var(--blue)" stroke-width="2"/><path d="M4 11h14" stroke="var(--blue)" stroke-width="2"/></svg></div><div><h3>We Store Your Documents</h3><p>Your documents are stored in our secure purpose-built facility in Riverside.</p></div></div>
<div class="abs step" style="top:1508px"><div class="ico"><svg width="22" height="22" viewBox="0 0 22 22"><path d="M4 8h12l-3-3M18 14H6l3 3" fill="none" stroke="var(--blue)" stroke-width="2"/></svg></div><div><h3>We Retrieve &amp; Deliver Your Documents</h3><p>When you need your documents, just call or email us and we'll get them to you.</p></div></div>
<div class="abs step" style="top:1614px"><div class="ico"><svg width="22" height="22" viewBox="0 0 22 22"><path d="M5 6h12M7 6l1 13h6l1-13M9 6V3h4v3" fill="none" stroke="var(--blue)" stroke-width="2"/></svg></div><div><h3>We Can Securely Destroy</h3><p>We can work with you on determining which documents can be securely destroyed and do this for you.</p></div></div>

<div class="abs how-photo" role="img" aria-label="Warehouse worker scanning archive boxes with a tablet"></div>

<!-- team -->
<h2 class="abs section-title" style="left:80px;top:1856px;width:512px;text-align:center">Our Team</h2>
<div class="abs member featured" style="left:80px"><div class="portrait" role="img" aria-label="Team member portrait"></div><h4>Surname Name</h4><p>Lorem ipsum is simply</p></div>
<div class="abs member" style="left:352px"><div class="portrait" role="img" aria-label="Team member portrait"></div><h4>Surname Name</h4><p>Lorem ipsum is simply</p></div>

<div class="abs team-cta">
  <h3>Lorem Ipsum is simply dummy text of the printing.</h3>
  <p>Lorem Ipsum is simply dummy text of the printing and typesetting.</p>
  <span class="btn-line">Contact us <svg width="26" height="10" viewBox="0 0 26 10"><path d="M0 5h24M19 1l4 4-4 4" stroke="#fff" stroke-width="1.5" fill="none"/></svg></span>
</div>

<!-- why choose us -->
<h2 class="abs section-title" style="left:0;top:2384px;width:1200px;text-align:center;font-size:38px">Why choose us</h2>
<div class="abs why-item" style="left:80px"><svg width="44" height="44" viewBox="0 0 44 44"><circle cx="22" cy="22" r="16" fill="none" stroke="var(--red)" stroke-width="3"/><path d="M11 33L33 11" stroke="var(--red)" stroke-width="3"/></svg><span>No lock in<br>contracts</span></div>
<div class="abs why-item" style="left:264px"><svg width="44" height="44" viewBox="0 0 44 44"><rect x="6" y="10" width="32" height="24" fill="none" stroke="var(--green)" stroke-width="3"/><circle cx="17" cy="20" r="4" fill="var(--green)"/><path d="M26 18h8M26 24h8" stroke="var(--green)" stroke-width="3"/></svg><span>Expert Staff</span></div>
<div class="abs why-item" style="left:448px"><svg width="44" height="44" viewBox="0 0 44 44"><rect x="4" y="14" width="22" height="16" fill="none" stroke="var(--orange)" stroke-width="3"/><path d="M26 19h8l5 6v5H26" fill="none" stroke="var(--orange)" stroke-width="3"/><circle cx="12" cy="33" r="3" fill="var(--orange)"/><circle cx="32" cy="33" r="3" fill="var(--orange)"/></svg><span>Speedy Retrievals</span></div>
<div class="abs why-item" style="left:632px"><svg width="44" height="44" viewBox="0 0 44 44"><rect x="6" y="8" width="32" height="22" fill="none" stroke="var(--sky)" stroke-width="3"/><path d="M16 36h12M22 30v6" stroke="var(--sky)" stroke-width="3"/></svg><span>Simple Online<br>Software</span></div>
<div class="abs why-item" style="left:816px"><svg width="44" height="44" viewBox="0 0 44 44"><path d="M8 22L22 8h14v14L22 36z" fill="none" stroke="#8b5fbf" stroke-width="3"/><circle cx="30" cy="14" r="3" fill="#8b5fbf"/></svg><span>Competitive Pricing</span></div>
<div class="abs why-item" style="left:1000px;width:120px"><svg width="44" height="44" viewBox="0 0 44 44"><rect x="4" y="12" width="36" height="20" fill="none" stroke="var(--blue-dark)" stroke-width="3"/><circle cx="22" cy="22" r="5" fill="none" stroke="var(--blue-dark)" stroke-width="3"/></svg><span>Money Back<br>Guarantee</span></div>

<!-- area of service -->
<section class="abs area" role="img" aria-label="Dimmed map of the service region"></section>
<div class="abs area-text"><h3>Area of Service</h3><p>We service the Riverside area, image of the coastal region and some basic text</p></div>

<!-- testimonials -->
<section class="abs testimonials">
  <h3>Testimonials</h3>
  <svg style="position:absolute;left:24px;top:150px" width="56" height="40" viewBox="0 0 56 40"><path d="M2 40V22C2 10 8 3 20 0v8c-6 2-8 6-8 12h8v20zM32 40V22C32 10 38 3 50 0v8c-6 2-8 6-8 12h8v20z" fill="#fff"/></svg>
  <div class="who">– Name Surname</div>
  <p class="quote-text">Lorem Ipsum is simply dummy text of the printing and typesetting industry. Lorem Ipsum has been the industry's standard dummy text ever since the 1500s, when an unknown printer took a galley of type and scrambled it to make a type specimen book. It has survived not only five centuries, but also the leap into electronic typesetting.</p>
  <div class="dots"><i></i><i></i><i></i></div>
</section>

<!-- footer -->
<footer class="abs footer">
  <div class="brand" style="left:80px;top:36px"><div class="mark"></div><div class="name" style="color:#fff">KEEPWELL STORAGE</div></div>
  <p class="abs small" style="left:80px;top:96px;width:240px">Lorem ipsum is simply dummy text of the printing and typesetting industry.</p>

  <h5 class="abs" style="left:436px;top:30px">Sitemap</h5>
  <div class="abs links" style="left:436px;top:76px">Home<br>Offsite Storage<br>Document Shredding</div>
  <div class="abs links" style="left:636px;top:76px">Digitisation<br>Archival Supplies<br>Contact</div>

  <h5 class="abs" style="left:800px;top:30px">Contact Info</h5>
  <div class="abs small" style="left:800px;top:80px;display:flex;gap:12px;width:300px">
    <svg width="14" height="18" viewBox="0 0 14 18" style="flex:none"><path d="M7 0a7 7 0 0 1 7 7c0 5-7 11-7 11S0 12 0 7a7 7 0 0 1 7-7z" fill="#fff"/><circle cx="7" cy="7" r="2.5" fill="var(--footer)"/></svg>
    <span>Lorem ipsum is simply dummy text of the printing and typesetting industry.</span>
  </div>
  <div class="abs small" style="left:800px;top:136px;display:flex;gap:12px">
    <svg width="14" height="14" viewBox="0 0 14 14"><path d="M2 1h3l1 3-1.5 1.2a8 8 0 0 0 4.3 4.3L10 8l3 1v3C7 13 1 7 2 1z" fill="#fff"/></svg>123 456 7890
  </div>
  <div class="abs small" style="left:800px;top:164px;display:flex;gap:12px">
    <svg width="14" height="12" viewBox="0 0 14 12"><rect x="0" y="1" width="14" height="10" fill="#fff"/><path d="M0 1l7 5 7-5" stroke="var(--footer)" fill="none"/></svg>info@keepwell_storage.com
  </div>
</footer>
<div class="abs copyright">KEEPWELL STORAGE – 2016. All Rights Reserved.</div>

</body>
</html>
```